Redesign for Real Estate Lead Generation Site

We are looking for a slight redesign for our real estate lead generation sites.

Here's one of our current sites: www.qdrhousefigures.com

The design should be simple as it is currently, remain only on one page, and nothing too detailed to where it may take a while to load/reload. We also have parallel sites, www.lmnhousefigures.com, www.lmnquicklistings.com, and a few others which all will end up utilizing the same template.

We've found that the majority of the site traffic will come from print advertising, not as much SEO. But also understand the more simple the site, the greater likelihood a user may find us through search engines. Another reason we want to keep it rather simple and clean.

The content on the page needs to remain the same, but with additional spaces for one written paragraph testimonial, and an area where we can incorporate a video. Originally, the ideal spot would be the open white space below the social media logos, but we are open to different ideas as you create the redesign.

A change in colors and simple graphics is what we're looking for most along with the testimonial / video additions. Also, we have a new logo we need incorporated into the site somewhere: http://www.brennoprintworks.com/KV-Crew-Properties.zip to download the file in different formates.

Here is our main site, www.kvcrewproperties.com through wordpress, so you can get an idea of what folks go to once they've signed up and received a confirm e-mail.

Please contact us if you have any questions. Good luck and thanks for submitting!

```html
<!DOCTYPE html>
<html lang="en">
<head>
<meta charset="utf-8">
<title>Fairfax VA Home Values — KV Crew Properties</title>
<link rel="stylesheet" href="https://fonts.googleapis.com/css2?family=Arimo:wght@400;700&display=swap">
<style>
  :root {
    --page: #ffffff;
    --ink: #333333;
    --ink-soft: #444444;
    --panel: #f0f0f0;
    --panel-join: #cbcbcb;
    --quote: #e6e6e6;
    --header-top: #4a4a4a;
    --header-bottom: #262626;
    --field-border: #b9c7d6;
    --field-bg: #ffffff;
    --accent-top: #fbc02d;
    --accent-bottom: #ef9a00;
    --social: #8a8a8a;
    --photo-fill: #a3a596;
    --video-fill: #8d9682;
  }
  * { box-sizing: border-box; margin: 0; padding: 0; }
  html, body { width: 1200px; height: 1049px; overflow: hidden; background: var(--page); }
  body { position: relative; font-family: "Arimo", "Helvetica Neue", Arial, sans-serif; color: var(--ink); }

  .brand { position: absolute; left: 155px; top: 33px; display: flex; align-items: center; gap: 6px; }
  .brand-mark { width: 36px; height: 36px; background: var(--ink); }
  .brand-name { font-size: 15px; font-weight: 700; color: var(--ink); line-height: 1; width: 70px; }

  .masthead {
    position: absolute; left: 141px; top: 92px; width: 920px; height: 59px; border-radius: 6px;
    background: linear-gradient(var(--header-top), var(--header-bottom));
  }
  .masthead h1 { position: absolute; left: 22px; top: 10px; font-size: 37px; font-weight: 700; color: #fff; letter-spacing: -0.3px; }
  .masthead-photo {
    position: absolute; left: 767px; top: 27px; width: 262px; height: 124px;
    background: var(--photo-fill);
  }

  .intro { position: absolute; left: 158px; top: 172px; width: 885px; font-size: 18.5px; font-weight: 700; line-height: 22.5px; color: var(--ink-soft); }

  .lead-form { position: absolute; left: 141px; top: 272px; width: 460px; height: 676px; background: var(--panel); border-radius: 6px; }
  .lead-form h2 { position: absolute; left: 18px; font-size: 20px; font-weight: 700; color: var(--ink); letter-spacing: -0.3px; }
  .lead-form label { position: absolute; font-size: 12px; font-weight: 700; color: var(--ink-soft); }
  .field {
    position: absolute; height: 33px; background: var(--field-bg); border: 1px solid var(--field-border);
    border-radius: 2px; box-shadow: inset 0 1px 3px rgba(0,0,0,0.12); font: 14px "Arimo", sans-serif; color: var(--ink); padding: 0 12px;
  }
  .select { display: flex; align-items: center; }
  .select::after {
    content: ""; position: absolute; right: 12px; top: 14px;
    border-left: 5px solid transparent; border-right: 5px solid transparent; border-top: 5px solid #888;
  }
  textarea.field { height: 90px; resize: none; }
  .submit {
    position: absolute; left: 280px; top: 623px; width: 156px; height: 38px; border: none; border-radius: 3px;
    background: linear-gradient(var(--accent-top), var(--accent-bottom)); color: #fff; font: 700 16px "Arimo", sans-serif;
  }

  .testimonial { position: absolute; left: 624px; top: 275px; width: 432px; height: 181px; background: var(--quote); border-radius: 4px; }
  .testimonial::after {
    content: ""; position: absolute; left: 336px; top: 181px;
    border-left: 0 solid transparent; border-right: 33px solid transparent; border-top: 29px solid var(--quote);
  }
  .testimonial blockquote { position: absolute; left: 19px; top: 37px; width: 390px; font-size: 14.5px; line-height: 19px; color: var(--ink); }
  .testimonial cite { position: absolute; right: 29px; top: 130px; font-size: 14.5px; font-weight: 700; font-style: normal; }

  .social { position: absolute; left: 620px; top: 509px; width: 439px; height: 67px; background: var(--panel-join); border-radius: 3px; }
  .social h3 { position: absolute; left: 19px; top: 21px; font-size: 22px; font-weight: 700; color: var(--ink-soft); }
  .social-links { position: absolute; left: 287px; top: 14px; display: flex; gap: 13px; list-style: none; }
  .social-links li { width: 36px; height: 36px; background: var(--social); border-radius: 4px; }

  .video { position: absolute; left: 620px; top: 612px; width: 439px; height: 336px; background: var(--panel); border-radius: 4px; }
  .video h3 { position: absolute; left: 16px; top: 14px; font-size: 18px; font-weight: 700; color: #111; }
  .video-frame {
    position: absolute; left: 17px; top: 44px; width: 404px; height: 247px;
    background: var(--video-fill);
  }
  .video-play { position: absolute; left: 173px; top: 86px; }
  .video-controls { position: absolute; left: 17px; top: 298px; width: 404px; height: 16px; }
  .time { position: absolute; font-size: 9px; color: var(--ink-soft); }

  .site-footer { position: absolute; left: 141px; top: 969px; width: 920px; height: 48px; background: var(--panel); border-radius: 4px; font-size: 13px; color: var(--ink); }
  .site-footer .copy { position: absolute; left: 23px; top: 17px; }
  .site-footer .contact { position: absolute; right: 21px; top: 17px; }
</style>
</head>
<body>
  <header>
    <div class="brand"><span class="brand-mark"></span><span class="brand-name">KV Crew Properties</span></div>
    <div class="masthead">
      <h1>Fairfax VA Home Values</h1>
    </div>
    <div class="masthead-photo" role="img" aria-label="Photo of a two-story suburban house with porch and landscaped yard"></div>
  </header>

  <p class="intro">Fill out the form below for a FREE Comparative Market Analysis Report from KV Crew Properties for an estimate of your home's current value. The more complete the form the easier it will be to provide an accurate report regarding the value of your home.</p>

  <form class="lead-form">
    <h2 style="top:17px">Personal Information</h2>
    <label style="left:18px;top:52px">Name</label>
    <input class="field" style="left:18px;top:72px;width:421px">
    <label style="left:18px;top:121px">Email</label>
    <input class="field" style="left:18px;top:143px;width:201px">
    <label style="left:236px;top:121px">Phone Number</label>
    <input class="field" style="left:236px;top:143px;width:202px">

    <h2 style="top:197px">Property Address</h2>
    <label style="left:18px;top:233px">Street Address</label>
    <input class="field" style="left:18px;top:252px;width:421px">
    <label style="left:18px;top:302px">City</label>
    <input class="field" style="left:18px;top:323px;width:121px">
    <label style="left:156px;top:302px">State</label>
    <div class="field select" style="left:156px;top:323px;width:132px">VA</div>
    <label style="left:307px;top:302px">Zip</label>
    <input class="field" style="left:307px;top:323px;width:131px">

    <h2 style="top:379px">Property Description</h2>
    <label style="left:18px;top:418px">Number of Bedroom</label>
    <div class="field select" style="left:18px;top:440px;width:120px">Any</div>
    <label style="left:156px;top:418px">Number of Bathrooms</label>
    <div class="field select" style="left:156px;top:440px;width:132px">Any</div>
    <label style="left:307px;top:418px">Condition</label>
    <div class="field select" style="left:307px;top:440px;width:131px">Any</div>

    <label style="left:18px;top:496px">Additional Comments</label>
    <textarea class="field" style="left:18px;top:519px;width:420px"></textarea>
    <button type="submit" class="submit">SIGN UP NOW</button>
  </form>

  <aside class="testimonial">
    <blockquote>Lena Ruth and Mira did such an amazing job making the sale of my Condo the easiest Real Estate transaction I have ever experienced. Thank you so much for making it all go so smoothly.</blockquote>
    <cite>Carla Wendt, July 2011</cite>
  </aside>

  <section class="social">
    <h3>Join Our Conversation:</h3>
    <ul class="social-links">
      <li aria-label="Social network link"></li>
      <li aria-label="Video channel link"></li>
      <li aria-label="Microblog link"></li>
    </ul>
  </section>

  <section class="video">
    <h3>Video Feature</h3>
    <div class="video-frame" role="img" aria-label="Video still of a two-story house on a green lawn with trees">
      <svg class="video-play" width="74" height="74" viewBox="0 0 74 74" aria-hidden="true">
        <circle cx="37" cy="37" r="35" fill="#fff" opacity="0.85"/>
        <circle cx="37" cy="37" r="29" fill="#f4a300"/>
        <path d="M29 23 L52 37 L29 51 Z" fill="#fff"/>
      </svg>
    </div>
    <svg class="video-controls" width="404" height="16" viewBox="0 0 404 16" aria-hidden="true">
      <path d="M7 3 L15 8 L7 13 Z" fill="#444"/>
      <rect x="35" y="5" width="203" height="6" rx="3" fill="#555"/>
      <rect x="35" y="5" width="100" height="6" rx="3" fill="#f4b000"/>
      <circle cx="135" cy="8" r="4" fill="#ddd" stroke="#666"/>
      <path d="M302 5 h3 l4 -3 v12 l-4 -3 h-3 Z" fill="#444"/>
      <rect x="316" y="6" width="52" height="4" rx="2" fill="#555"/>
      <rect x="386" y="3" width="10" height="10" fill="none" stroke="#444" stroke-width="1.5" stroke-dasharray="3 4"/>
    </svg>
    <span class="time" style="left:262px;top:298px">3:47 / 9:29</span>
  </section>

  <footer class="site-footer">
    <span class="copy">© 2010 KV Crew Properties</span>
    <span class="contact">KV Crew Properties :: Harborline Realty Group :: 877-555-0142 :: info@kvcrewproperties.com</span>
  </footer>
</body>
</html>
```